Zombie Themed Web Site Design

I am looking for a web page design for a web site that will be selling zombie themed items.

Starting out we are selling one product, a zombie combat patch so I would like the web design to be based of it, but the attached image should only be a starting point. Please do not hesitate to be as creative as possible.

The site design should be family friendly but defiantly be zombie themed. For the color schema it does not have to be the black and reds that the patch is based on for the page theme.

The Home page should be a page of shear zombie awesomeness that points to the products.

That other pages that are to be static, are the:
About Us, Gallery, Refund Policy, Privacy Policy, Terms & Conditions, Shipping and Delivery and Contact us pages.

-LINK- to the web site (there is nothing there yet)
http://ghoulbrigadegear.example

-LINK- to the zombie patch image
https://files.quillnest.example/s/k7m2p9q4r1t8vwx/Zombie.jpg

PSD file output is just fine, HTML and CSS files are even better.

If there are any questions, please leave a comment.
Updates

From the submission that I have been receiving, I need to clarifyjust what I am looking for. The theme of the site should be less of zombies risingout of the grave and eating people’s brains, and more a group of peoplethat have formed together (a “task force” if that helps) to hunt and kill zombies.I hope that this helps.

-Marcus    

Industry/Entity Type

Shipping

Requirements
Nice to have
• The use of a military font in the design would awsome.

```html
<!DOCTYPE html>
<html lang="en">
<head>
<meta charset="utf-8">
<title>Ghoul Brigade Gear</title>
<link rel="stylesheet" href="https://fonts.googleapis.com/css2?family=Black+Ops+One&family=Oswald:wght@500&family=Arimo:wght@400&display=swap">
<style>
:root{
  --ink:#0d0d0d;
  --night:#161616;
  --blood:#e3260c;
  --blood-dark:#b81a05;
  --paper:#ffffff;
  --hazard:#f4ee0a;
  --moss:#3c7a3a;
  --muted:#8a8a8a;
  --price:#e3260c;
}
*{margin:0;padding:0;box-sizing:border-box}
html,body{width:1200px;height:1114px;overflow:hidden}
body{
  position:relative;
  background:var(--ink);
  font-family:"Arimo",Arial,sans-serif;
  color:#fff;
}
.backdrop{
  position:absolute;inset:0;
  background:radial-gradient(ellipse at 50% 40%,#4a4d4d 0%,#2c2e2e 45%,#121212 85%);
}
.backdrop-floor{
  position:absolute;left:0;right:0;bottom:0;height:140px;
  background:linear-gradient(#121212,#060606);
}
.topbar{
  position:absolute;top:14px;left:720px;width:290px;
  font-size:11px;display:flex;align-items:center;gap:5px;
}
.topbar a{color:#fff}
.topbar .cart{margin-left:24px;display:flex;align-items:center;gap:4px}
.masthead{
  position:absolute;left:188px;top:36px;width:822px;height:97px;
  background:linear-gradient(90deg,var(--blood) 0%,#d9230b 70%,#c21d07 100%);
}
.brand{
  position:absolute;left:30px;top:20px;
  font-family:"Black Ops One",sans-serif;font-size:28px;color:var(--hazard);
  display:flex;align-items:center;gap:10px;letter-spacing:.5px;
}
.brand .mark{width:14px;height:14px;background:var(--hazard)}
.shipping-note{
  position:absolute;right:0;top:68px;height:24px;width:290px;
  background:var(--ink);display:flex;align-items:center;gap:6px;
  padding-left:10px;font-size:9.5px;
}
.mainnav{
  position:absolute;left:188px;top:139px;width:822px;height:32px;
  background:var(--ink);display:flex;align-items:center;
  padding-left:35px;
  font-family:"Oswald",sans-serif;font-size:12px;text-transform:uppercase;
}
.mainnav a{color:#fff;text-decoration:none}
.mainnav a.current{color:var(--blood)}
.mainnav .sep{margin:0 20px;color:#fff}
.hero{
  position:absolute;left:190px;top:186px;width:818px;height:262px;
  background:#000;
}
.hero-kicker{
  position:absolute;left:52px;top:68px;
  font-family:"Black Ops One",sans-serif;font-size:28px;color:var(--hazard);
}
.hero-title{
  position:absolute;left:55px;top:128px;
  font-family:"Black Ops One",sans-serif;font-size:26px;color:#fff;letter-spacing:.5px;
}
.shop-now{
  position:absolute;left:68px;top:190px;width:150px;height:30px;
  background:var(--moss);display:flex;align-items:center;gap:10px;padding-left:12px;
  font-family:"Black Ops One",sans-serif;font-size:15px;color:#fff;text-decoration:none;
  clip-path:polygon(4% 0,100% 8%,96% 100%,0 92%);
}
.hero-visual{
  position:absolute;left:560px;top:24px;width:180px;height:214px;
  background:linear-gradient(160deg,#2a2d2c,#161818 60%,#2a1010);
}
.catalog{
  position:absolute;left:188px;top:464px;width:822px;height:549px;
  background:var(--paper);color:#000;
}
.section-tag{
  position:absolute;left:8px;top:16px;width:220px;height:34px;
  background:var(--ink);
  font-family:"Black Ops One",sans-serif;font-size:15px;font-weight:400;color:#fff;
  padding:9px 0 0 50px;
  clip-path:polygon(0 8%,92% 0,100% 50%,94% 100%,2% 94%);
}
.product{position:absolute;width:150px;text-align:center}
.product-image{
  width:137px;height:120px;margin:0 auto;border:1px solid #d4d4d4;
  padding:3px;background:#fff;
}
.product-image span{display:block;width:100%;height:100%}
.art-patch{background:linear-gradient(160deg,#2a3230,#131818 60%,#5a1010)}
.art-hunter{background:radial-gradient(circle,#fff 0%,#f3d9d6 40%,#d8221a 75%,#f2f2f2 100%)}
.art-warning{background:linear-gradient(#f4ee0a,#ece50a)}
.art-love{background:linear-gradient(#f7f7f7,#e6e6e6)}
.product-name{font-size:11px;margin-top:10px}
.product-price{font-size:11px;margin-top:3px}
.product-price s{color:var(--muted)}
.product-price b{font-weight:400;color:var(--price)}
.add-cart{
  margin:10px auto 0;width:110px;height:32px;background:var(--blood);
  display:flex;align-items:center;justify-content:center;gap:5px;
  font-family:"Oswald",sans-serif;font-size:11px;color:#000;
  clip-path:polygon(3% 6%,98% 0,100% 90%,2% 100%);
}
.site-footer{
  position:absolute;left:188px;top:1037px;width:822px;height:56px;
  background:var(--blood);font-size:9px;color:#000;
}
.footer-links{position:absolute;left:30px;top:10px}
.footer-copy{position:absolute;left:30px;top:26px}
.footer-legal{position:absolute;right:22px;top:20px}
.footer-legal a{color:#000}
</style>
</head>
<body>
<div class="backdrop" role="img" aria-label="Misty graveyard with tombstones at dusk"></div>
<div class="backdrop-floor"></div>

<div class="topbar">
  <span>Welcome User,</span> <a href="#">Login</a> | <a href="#">Register</a>
  <span class="cart">
    <svg width="18" height="16" viewBox="0 0 20 18"><path d="M1 2h3l3 9h9l2-7H6" fill="none" stroke="#fff" stroke-width="2"/><circle cx="8" cy="15" r="1.6" fill="#fff"/><circle cx="15" cy="15" r="1.6" fill="#fff"/></svg>
    Cart has $0.00
  </span>
</div>

<header class="masthead">
  <div class="brand"><span class="mark"></span>Ghoul Brigade Gear</div>
  <div class="shipping-note">
    <svg width="34" height="20" viewBox="0 0 34 20"><rect x="1" y="3" width="20" height="12" fill="#d42"/><path d="M21 7h7l4 5v3H21z" fill="#eee"/><circle cx="8" cy="16" r="3" fill="#fff"/><circle cx="26" cy="16" r="3" fill="#fff"/></svg>
    Free Shipping and Delivery on products above $59.99
  </div>
</header>

<nav class="mainnav">
  <a class="current" href="#">Home</a><span class="sep">|</span>
  <a href="#">New Products</a><span class="sep">|</span>
  <a href="#">Specials</a><span class="sep">|</span>
  <a href="#">My Account</a><span class="sep">|</span>
  <a href="#">About Us</a><span class="sep">|</span>
  <a href="#">Contact Us</a><span class="sep">|</span>
  <a href="#">Gallery</a>
</nav>

<section class="hero">
  <div class="hero-kicker">ZOMBIE WINS HERE</div>
  <div class="hero-title">GET THE BEST MERCHANDICE!</div>
  <a class="shop-now" href="#">
    <svg width="10" height="18" viewBox="0 0 10 18"><path d="M0 0l10 9-10 9z" fill="#f4ee0a"/></svg>SHOP NOW
  </a>
  <div class="hero-visual" role="img" aria-label="Featured product photo of the task force combat patch"></div>
</section>

<main class="catalog">
  <h2 class="section-tag">BESTSELLERS</h2>

  <div class="product" style="left:20px;top:62px"><div class="product-image"><span class="art-patch" role="img" aria-label="Combat patch product photo"></span></div><p class="product-name">ZOMBIE tag</p><p class="product-price"><s>$78.00</s> <b>$45.99</b></p><div class="add-cart"><svg width="14" height="12" viewBox="0 0 20 18"><path d="M1 2h3l3 9h9l2-7H6" fill="none" stroke="#000" stroke-width="2.4"/><circle cx="8" cy="15" r="2" fill="#000"/><circle cx="15" cy="15" r="2" fill="#000"/></svg>ADD TO CART</div></div>
  <div class="product" style="left:177px;top:62px"><div class="product-image"><span class="art-patch" role="img" aria-label="Combat patch product photo"></span></div><p class="product-name">ZOMBIE tag</p><p class="product-price"><s>$78.00</s> <b>$45.99</b></p><div class="add-cart"><svg width="14" height="12" viewBox="0 0 20 18"><path d="M1 2h3l3 9h9l2-7H6" fill="none" stroke="#000" stroke-width="2.4"/><circle cx="8" cy="15" r="2" fill="#000"/><circle cx="15" cy="15" r="2" fill="#000"/></svg>ADD TO CART</div></div>
  <div class="product" style="left:336px;top:62px"><div class="product-image"><span class="art-hunter" role="img" aria-label="Zombie hunter coaster artwork"></span></div><p class="product-name">Zombie Kill Zone Tile Coaster</p><p class="product-price"><s>$78.00</s> <b>$45.99</b></p><div class="add-cart"><svg width="14" height="12" viewBox="0 0 20 18"><path d="M1 2h3l3 9h9l2-7H6" fill="none" stroke="#000" stroke-width="2.4"/><circle cx="8" cy="15" r="2" fill="#000"/><circle cx="15" cy="15" r="2" fill="#000"/></svg>ADD TO CART</div></div>
  <div class="product" style="left:493px;top:62px"><div class="product-image"><span class="art-warning" role="img" aria-label="Yellow kill zone warning sign"></span></div><p class="product-name">ZOMBIE tag</p><p class="product-price"><s>$78.00</s> <b>$45.99</b></p><div class="add-cart"><svg width="14" height="12" viewBox="0 0 20 18"><path d="M1 2h3l3 9h9l2-7H6" fill="none" stroke="#000" stroke-width="2.4"/><circle cx="8" cy="15" r="2" fill="#000"/><circle cx="15" cy="15" r="2" fill="#000"/></svg>ADD TO CART</div></div>
  <div class="product" style="left:651px;top:62px"><div class="product-image"><span class="art-love" role="img" aria-label="I love zombies coaster artwork"></span></div><p class="product-name">I LOVE ZOMBIES Tile Coaster</p><p class="product-price"><s>$78.00</s> <b>$45.99</b></p><div class="add-cart"><svg width="14" height="12" viewBox="0 0 20 18"><path d="M1 2h3l3 9h9l2-7H6" fill="none" stroke="#000" stroke-width="2.4"/><circle cx="8" cy="15" r="2" fill="#000"/><circle cx="15" cy="15" r="2" fill="#000"/></svg>ADD TO CART</div></div>

  <div class="product" style="left:20px;top:302px"><div class="product-image"><span class="art-hunter" role="img" aria-label="Zombie hunter coaster artwork"></span></div><p class="product-name">ZOMBIE tag</p><p class="product-price"><s>$78.00</s> <b>$45.99</b></p><div class="add-cart"><svg width="14" height="12" viewBox="0 0 20 18"><path d="M1 2h3l3 9h9l2-7H6" fill="none" stroke="#000" stroke-width="2.4"/><circle cx="8" cy="15" r="2" fill="#000"/><circle cx="15" cy="15" r="2" fill="#000"/></svg>ADD TO CART</div></div>
  <div class="product" style="left:177px;top:302px"><div class="product-image"><span class="art-warning" role="img" aria-label="Yellow kill zone warning sign"></span></div><p class="product-name">I LOVE ZOMBIES Tile Coaster</p><p class="product-price"><s>$78.00</s> <b>$45.99</b></p><div class="add-cart"><svg width="14" height="12" viewBox="0 0 20 18"><path d="M1 2h3l3 9h9l2-7H6" fill="none" stroke="#000" stroke-width="2.4"/><circle cx="8" cy="15" r="2" fill="#000"/><circle cx="15" cy="15" r="2" fill="#000"/></svg>ADD TO CART</div></div>
  <div class="product" style="left:336px;top:302px"><div class="product-image"><span class="art-patch" role="img" aria-label="Combat patch product photo"></span></div><p class="product-name">ZOMBIE tag</p><p class="product-price"><s>$78.00</s> <b>$45.99</b></p><div class="add-cart"><svg width="14" height="12" viewBox="0 0 20 18"><path d="M1 2h3l3 9h9l2-7H6" fill="none" stroke="#000" stroke-width="2.4"/><circle cx="8" cy="15" r="2" fill="#000"/><circle cx="15" cy="15" r="2" fill="#000"/></svg>ADD TO CART</div></div>
  <div class="product" style="left:493px;top:302px"><div class="product-image"><span class="art-warning" role="img" aria-label="Yellow kill zone warning sign"></span></div><p class="product-name">I LOVE ZOMBIES Tile Coaster</p><p class="product-price"><s>$78.00</s> <b>$45.99</b></p><div class="add-cart"><svg width="14" height="12" viewBox="0 0 20 18"><path d="M1 2h3l3 9h9l2-7H6" fill="none" stroke="#000" stroke-width="2.4"/><circle cx="8" cy="15" r="2" fill="#000"/><circle cx="15" cy="15" r="2" fill="#000"/></svg>ADD TO CART</div></div>
  <div class="product" style="left:651px;top:302px"><div class="product-image"><span class="art-patch" role="img" aria-label="Combat patch product photo"></span></div><p class="product-name">ZOMBIE tag</p><p class="product-price"><s>$78.00</s> <b>$45.99</b></p><div class="add-cart"><svg width="14" height="12" viewBox="0 0 20 18"><path d="M1 2h3l3 9h9l2-7H6" fill="none" stroke="#000" stroke-width="2.4"/><circle cx="8" cy="15" r="2" fill="#000"/><circle cx="15" cy="15" r="2" fill="#000"/></svg>ADD TO CART</div></div>
</main>

<footer class="site-footer">
  <p class="footer-links">About Us / Gallery / Refund Policy / Shipping and Delivery / Contact</p>
  <p class="footer-copy">All Content Copyright © 1999-2013 ghoulbrigadegear.example</p>
  <p class="footer-legal"><a href="#">Privacy Policy</a> | <a href="#">Terms of Use</a> | <a href="#">FAQ</a></p>
</footer>
</body>
</html>
```